Need design for an App.

The app in question is related to security and crime events with real time feed, engagement with friends and posting pictures, we want a sleak, minimal style. There are 11 or 12 screens to be made. We are adding video file as suggestion. We are not sure about colors so we accept suggestions. We are also adding the logo.

Reason: Just giving more time to designers. Thanks.

Industry/Entity Type

Security

Font styles to use
Sans Serif

Requirements
Must have
• The app must have a Login view; a new user view (with nickname, email and pass); a retrieve pass view; a menu view with options for alert configuration, send emergency alert and send report, a feed view with the most popular reports (3 worldwide at the top and near reports after), a profile view with avatar and personal reports, a send emergency alert view with a camera view; a configuration view when the user can put up to 5 contacts to send the alert to them;a send report view with camera and options to configure the camera; a edit report view where the user can see the 3 photos he will update and add a comment of those photos.
Nice to have
• Check the files we are open minds
Should not have
• old design

```html
<!DOCTYPE html>
<html lang="en">
<head>
<meta charset="utf-8">
<title>Vigilo – Sign-in Screens</title>
<link rel="stylesheet" href="https://fonts.googleapis.com/css2?family=Abel&family=Ubuntu:wght@400&display=swap">
<style>
  :root {
    --canvas: #ffffff;
    --screen-dark: #0b0b0c;
    --screen-mid: #2a2a2d;
    --brand-red: #c41e3a;
    --ink-white: #ffffff;
    --ink-grey: #2b2b2b;
    --dot-off: #e8e8e8;
  }
  * { box-sizing: border-box; margin: 0; padding: 0; }
  html, body { width: 1200px; height: 1000px; overflow: hidden; background: var(--canvas); }
  .stage { position: relative; width: 1200px; height: 1000px; }

  .screen {
    position: absolute; overflow: hidden; color: var(--ink-white);
    font-family: "Abel", sans-serif;
  }
  .screen__backdrop {
    position: absolute; inset: 0;
    background:
      radial-gradient(ellipse at 50% 35%, rgba(90,90,95,.45), transparent 60%),
      linear-gradient(180deg, var(--screen-mid) 0%, #151516 45%, var(--screen-dark) 100%);
  }
  .screen > *:not(.screen__backdrop) { position: absolute; }

  .status-bar { left: 8px; right: 8px; display: flex; align-items: center; font-size: 12px; font-family: "Ubuntu", sans-serif; }
  .status-bar__left, .status-bar__right { display: flex; align-items: center; gap: 5px; }
  .status-bar__right { margin-left: auto; }
  .status-bar__pill { position: absolute; left: 50%; top: 4px; width: 28px; height: 5px; margin-left: -14px; border-radius: 3px; background: #8a8a8a; }

  .brand-card {
    background: var(--ink-white); border-radius: 10px;
    display: flex; flex-direction: column; align-items: center; justify-content: center; gap: 10%;
  }
  .brand-card__mark { background: var(--brand-red); border-radius: 12px; }
  .brand-card__name { font-family: "Abel", sans-serif; color: var(--ink-grey); line-height: 1; }

  .pager { left: 0; right: 0; display: flex; justify-content: center; gap: 3px; }
  .pager span { width: 4px; height: 4px; border-radius: 50%; background: var(--dot-off); }
  .pager span:first-child { background: var(--brand-red); }

  .heading { left: 0; right: 0; text-align: center; letter-spacing: .5px; }
  .note { left: 0; right: 0; text-align: center; font-family: "Ubuntu", sans-serif; font-size: 11px; line-height: 14px; letter-spacing: .3px; }

  .field {
    background: var(--ink-white); border-radius: 12px; color: var(--brand-red);
    font-family: "Ubuntu", sans-serif; text-align: center; display: flex; align-items: center; justify-content: center;
    box-shadow: 0 0 0 2px #000, 0 0 0 3px #fff;
  }
  .button {
    background: var(--brand-red); border-radius: 11px; color: var(--ink-white);
    display: flex; align-items: center; justify-content: center; letter-spacing: .5px;
  }
  .legal { left: 0; right: 0; text-align: center; font-family: "Ubuntu", sans-serif; font-size: 7px; letter-spacing: .2px; }
  .home-bar { left: 50%; width: 26px; margin-left: -13px; height: 4px; border-radius: 2px; background: #8a8a8a; }

  /* Login */
  .screen--login { left: 48px; top: 218px; width: 302px; height: 530px; }
  .screen--login .status-bar { top: 4px; }
  .screen--login .brand-card { left: 82px; top: 30px; width: 138px; height: 197px; }
  .screen--login .brand-card__mark { width: 96px; height: 96px; }
  .screen--login .brand-card__name { font-size: 44px; }
  .screen--login .pager { top: 250px; }
  .screen--login .heading { top: 271px; font-size: 13px; }
  .screen--login .field { left: 25px; width: 252px; height: 31px; font-size: 12px; }
  .screen--login .button { height: 28px; font-size: 15px; }
  .screen--login .legal { top: 505px; }
  .screen--login .home-bar { top: 518px; }

  /* Register */
  .screen--register { left: 437px; top: 153px; width: 348px; height: 612px; }
  .screen--register .status-bar { top: 5px; }
  .screen--register .brand-card { left: 121px; top: 35px; width: 109px; height: 155px; }
  .screen--register .brand-card__mark { width: 76px; height: 76px; border-radius: 10px; }
  .screen--register .brand-card__name { font-size: 36px; }
  .screen--register .pager { top: 210px; }
  .screen--register .heading { top: 237px; font-size: 14px; }
  .screen--register .field { left: 30px; width: 289px; height: 34px; font-size: 14px; }
  .screen--register .button { left: 65px; top: 519px; width: 219px; height: 32px; font-size: 17px; border-radius: 13px; }
  .screen--register .legal { top: 584px; font-size: 8px; }
  .screen--register .home-bar { top: 598px; }

  /* Reset */
  .screen--reset { left: 863px; top: 222px; width: 300px; height: 528px; }
  .screen--reset .status-bar { top: 4px; }
  .screen--reset .brand-card { left: 103px; top: 30px; width: 94px; height: 133px; border-radius: 8px; }
  .screen--reset .brand-card__mark { width: 66px; height: 66px; border-radius: 9px; }
  .screen--reset .brand-card__name { font-size: 31px; }
  .screen--reset .pager { top: 181px; }
  .screen--reset .heading { top: 211px; font-size: 12px; }
  .screen--reset .note { top: 264px; }
  .screen--reset .field { left: 25px; top: 338px; width: 249px; height: 31px; font-size: 12px; }
  .screen--reset .button { left: 56px; top: 400px; width: 188px; height: 28px; font-size: 15px; }
  .screen--reset .legal { top: 503px; }
  .screen--reset .home-bar { top: 517px; }
</style>
</head>
<body>
<div class="stage">

  <!-- Login screen -->
  <section class="screen screen--login">
    <div class="screen__backdrop" role="img" aria-label="Dark blurred photo of city buildings at night"></div>
    <div class="status-bar">
      <div class="status-bar__left">
        <svg width="26" height="6" viewBox="0 0 26 6"><g fill="#fff"><circle cx="3" cy="3" r="2.5"/><circle cx="8.5" cy="3" r="2.5"/><circle cx="14" cy="3" r="2.5"/><circle cx="19.5" cy="3" r="2.5"/></g><circle cx="25" cy="3" r="2" fill="none" stroke="#fff" stroke-width=".8"/></svg>
        <span>Nexa</span>
        <svg width="11" height="8" viewBox="0 0 11 8"><path d="M.5 3a7 7 0 0 1 10 0M2.3 4.8a4.5 4.5 0 0 1 6.4 0" fill="none" stroke="#fff" stroke-width="1.1"/><circle cx="5.5" cy="6.8" r="1" fill="#fff"/></svg>
      </div>
      <span class="status-bar__pill"></span>
      <div class="status-bar__right">
        <svg width="6" height="9" viewBox="0 0 6 9"><path d="M1 2.5l4 4-2 2V.5l2 2-4 4" fill="none" stroke="#fff" stroke-width=".8"/></svg>
        <span>82%</span>
        <svg width="26" height="9" viewBox="0 0 26 9"><rect x=".5" y=".5" width="20" height="8" rx="1.5" fill="none" stroke="#fff"/><rect x="2" y="2" width="15" height="5" fill="#fff"/><rect x="21.5" y="3" width="1.3" height="3" fill="#fff"/><path d="M25 1l-1.6 3.5h1.4L23.5 8" fill="none" stroke="#fff" stroke-width=".8"/></svg>
      </div>
    </div>
    <div class="brand-card"><span class="brand-card__mark"></span><span class="brand-card__name">vigilo</span></div>
    <div class="pager"><span></span><span></span><span></span><span></span><span></span><span></span></div>
    <h2 class="heading">LOGIN WITH YOUR CREDENTIALS</h2>
    <div class="field" style="top:302px">User Name</div>
    <div class="field" style="top:353px">Password</div>
    <div class="button" style="left:25px;top:408px;width:102px">LOGIN</div>
    <div class="button" style="left:171px;top:408px;width:104px">FORGET?</div>
    <div class="button" style="left:56px;top:453px;width:189px">NOT A MEMBER? SIGN UP</div>
    <p class="legal">COPYRIGHT ©2014 VIGILO. ALL RIGHTS RESERVED</p>
    <span class="home-bar"></span>
  </section>

  <!-- Register screen -->
  <section class="screen screen--register">
    <div class="screen__backdrop" role="img" aria-label="Dark blurred photo of city buildings at night"></div>
    <div class="status-bar">
      <div class="status-bar__left">
        <svg width="30" height="7" viewBox="0 0 26 6"><g fill="#fff"><circle cx="3" cy="3" r="2.5"/><circle cx="8.5" cy="3" r="2.5"/><circle cx="14" cy="3" r="2.5"/><circle cx="19.5" cy="3" r="2.5"/></g><circle cx="25" cy="3" r="2" fill="none" stroke="#fff" stroke-width=".8"/></svg>
        <span>Nexa</span>
        <svg width="13" height="9" viewBox="0 0 11 8"><path d="M.5 3a7 7 0 0 1 10 0M2.3 4.8a4.5 4.5 0 0 1 6.4 0" fill="none" stroke="#fff" stroke-width="1.1"/><circle cx="5.5" cy="6.8" r="1" fill="#fff"/></svg>
      </div>
      <span class="status-bar__pill"></span>
      <div class="status-bar__right">
        <svg width="7" height="10" viewBox="0 0 6 9"><path d="M1 2.5l4 4-2 2V.5l2 2-4 4" fill="none" stroke="#fff" stroke-width=".8"/></svg>
        <span>82%</span>
        <svg width="30" height="10" viewBox="0 0 26 9"><rect x=".5" y=".5" width="20" height="8" rx="1.5" fill="none" stroke="#fff"/><rect x="2" y="2" width="15" height="5" fill="#fff"/><rect x="21.5" y="3" width="1.3" height="3" fill="#fff"/><path d="M25 1l-1.6 3.5h1.4L23.5 8" fill="none" stroke="#fff" stroke-width=".8"/></svg>
      </div>
    </div>
    <div class="brand-card"><span class="brand-card__mark"></span><span class="brand-card__name">vigilo</span></div>
    <div class="pager"><span></span><span></span><span></span><span></span><span></span><span></span></div>
    <h2 class="heading">REGISTER WITH BELOW DETAILS</h2>
    <div class="field" style="top:278px">User Name</div>
    <div class="field" style="top:337px">Nick Name</div>
    <div class="field" style="top:396px">Email</div>
    <div class="field" style="top:455px">Password</div>
    <div class="button">REGISTER</div>
    <p class="legal">COPYRIGHT ©2014 VIGILO. ALL RIGHTS RESERVED</p>
    <span class="home-bar"></span>
  </section>

  <!-- Password reset screen -->
  <section class="screen screen--reset">
    <div class="screen__backdrop" role="img" aria-label="Dark blurred photo of city buildings at night"></div>
    <div class="status-bar">
      <div class="status-bar__left">
        <svg width="26" height="6" viewBox="0 0 26 6"><g fill="#fff"><circle cx="3" cy="3" r="2.5"/><circle cx="8.5" cy="3" r="2.5"/><circle cx="14" cy="3" r="2.5"/><circle cx="19.5" cy="3" r="2.5"/></g><circle cx="25" cy="3" r="2" fill="none" stroke="#fff" stroke-width=".8"/></svg>
        <span>Nexa</span>
        <svg width="11" height="8" viewBox="0 0 11 8"><path d="M.5 3a7 7 0 0 1 10 0M2.3 4.8a4.5 4.5 0 0 1 6.4 0" fill="none" stroke="#fff" stroke-width="1.1"/><circle cx="5.5" cy="6.8" r="1" fill="#fff"/></svg>
      </div>
      <span class="status-bar__pill"></span>
      <div class="status-bar__right">
        <svg width="6" height="9" viewBox="0 0 6 9"><path d="M1 2.5l4 4-2 2V.5l2 2-4 4" fill="none" stroke="#fff" stroke-width=".8"/></svg>
        <span>82%</span>
        <svg width="26" height="9" viewBox="0 0 26 9"><rect x=".5" y=".5" width="20" height="8" rx="1.5" fill="none" stroke="#fff"/><rect x="2" y="2" width="15" height="5" fill="#fff"/><rect x="21.5" y="3" width="1.3" height="3" fill="#fff"/><path d="M25 1l-1.6 3.5h1.4L23.5 8" fill="none" stroke="#fff" stroke-width=".8"/></svg>
      </div>
    </div>
    <div class="brand-card"><span class="brand-card__mark"></span><span class="brand-card__name">vigilo</span></div>
    <div class="pager"><span></span><span></span><span></span><span></span><span></span><span></span></div>
    <h2 class="heading">FORGET PASSWORD? FILL BELOW DETIALS</h2>
    <p class="note">Enter your email address to receive<br>Instructions on how to change<br>your password.</p>
    <div class="field">Email</div>
    <div class="button">SUBMIT</div>
    <p class="legal">COPYRIGHT ©2014 VIGILO. ALL RIGHTS RESERVED</p>
    <span class="home-bar"></span>
  </section>

</div>
</body>
</html>
```